Fund Harbor

We need desigin for our main page(concept will be used for other pages also).
We already have a logo, and moqup of our main page(see attch).
You could change layers and positions on moqup, but please use logo, and its colors in design creating. (We have logo in different colors, i attached 2 samples, so you could use also another colors if you wish).

Our bussinees will be something similar to LaunchPeak or Backwise.co, but with some special features. So main idea: start-ups, donations, investemnets

Designs were prefer:
http://backwise.co/
http://www.launchpeak.com/

Target Market(s)

Clients are middle aged persons, who interested in new start-ups, investments and so on.

Requirements
Must have
• Design must be neat

```html
<!DOCTYPE html>
<html lang="en">
<head>
<meta charset="utf-8">
<title>Fund Harbor</title>
<link href="https://fonts.googleapis.com/css2?family=Roboto+Condensed:wght@400;700&family=Open+Sans:wght@400;600;700&display=swap" rel="stylesheet">
<style>
:root{
  --blue-top:#1d6aa6;
  --blue-mid:#154f7f;
  --blue-deep:#0f3553;
  --navy:#12384f;
  --green:#7dc242;
  --red:#e02020;
  --grey-band:#d3d4d6;
  --grey-tab:#d9dadc;
  --page:#fafbfc;
  --card:#f1f2f5;
  --white:#ffffff;
  --text-dark:#10232e;
}
*{box-sizing:border-box;margin:0;padding:0}
html,body{width:768px;height:1200px;overflow:hidden}
body{position:relative;background:var(--page);font-family:"Roboto Condensed",Arial,sans-serif;color:var(--white)}
.abs{position:absolute}
.blue-grad{background:linear-gradient(to bottom,var(--blue-top),var(--blue-mid) 60%,var(--blue-deep))}

/* header */
.top-strip{left:0;top:0;width:768px;height:6px;background:var(--grey-band)}
.header{left:0;top:6px;width:768px;height:93px}
.header-rule{left:0;top:99px;width:768px;height:12px;background:var(--grey-band)}
.account-tab{top:5px;height:23px;background:var(--grey-tab);border-radius:0 0 5px 5px;color:#33424c;font-size:10px;display:flex;align-items:center;justify-content:center}
.tab-login{left:506px;width:74px}
.tab-register{left:586px;width:76px}
.brand{left:77px;top:28px;display:flex;align-items:center;gap:10px}
.brand-mark{width:46px;height:46px;border-radius:50%;background:var(--white)}
.brand-name{font-size:36px;font-weight:700;line-height:1;color:var(--white)}
.tagline{left:171px;top:67px;font-family:"Open Sans",Arial,sans-serif;font-size:9px;letter-spacing:.5px;color:var(--white)}
.search{left:452px;top:63px;width:130px;height:14px;background:var(--white);border-radius:7px;color:#222;font-size:7px;padding-left:9px;line-height:14px}
.search-clear{position:absolute;right:3px;top:3px;width:8px;height:8px;border-radius:50%;background:#333}
.language{left:601px;top:63px;width:59px;height:14px;background:var(--white);border-radius:7px;color:#222;font-size:7px;padding-left:7px;line-height:14px}
.language svg{position:absolute;right:5px;top:3px}

/* intro */
.stats{left:91px;top:134px;width:225px;height:252px;border-radius:8px;overflow:hidden;list-style:none}
.stats li{height:36px;display:flex;align-items:center;gap:8px;padding-left:14px;font-size:15px;border-bottom:1px solid #4f9a4a}
.stats li:last-child{border-bottom:none}
.tick{width:19px;height:19px;border-radius:50%;background:var(--green);display:flex;align-items:center;justify-content:center;flex:none}
.nav-btn{top:138px;height:48px;border-radius:8px;font-size:12px;display:flex;align-items:center;justify-content:center;box-shadow:inset 0 2px 0 #4f8fc4}
.video{left:329px;top:194px;width:334px;height:191px;background:#f0f1f3;border:1px solid #9a9da0}
.video-bar{position:absolute;left:0;bottom:0;width:100%;height:22px;background:#d0d1d3;display:flex;align-items:center;padding:0 8px;gap:10px}
.play{width:15px;height:15px;background:#3e4144;display:flex;align-items:center;justify-content:center}
.progress{flex:1;height:5px;background:var(--white);position:relative}
.progress span{position:absolute;left:0;top:0;height:5px;width:59%;background:var(--red)}
.screen-btn{width:18px;height:11px;border:2px solid #f4f4f4;background:#c4c5c7}

/* band */
.band-grey{left:0;top:436px;width:768px;height:111px;background:var(--grey-band)}
.band{left:0;top:439px;width:768px;height:90px}
.band-mark{left:324px;top:424px;width:120px;height:120px;border-radius:50%;background:var(--navy);border:6px solid #c8cbce}

/* projects */
.category{top:591px;height:41px;border-radius:7px;font-size:15px;display:flex;align-items:center;justify-content:center;box-shadow:inset 0 2px 0 #4f8fc4}
.card{top:643px;width:135px;height:211px;background:var(--card);border:1.5px solid var(--navy);border-radius:6px;color:var(--text-dark);text-align:center}
.stars{position:absolute;top:4px;left:0;width:100%;font-size:14px;letter-spacing:2px;color:var(--navy)}
.card-title{position:absolute;top:25px;width:100%;font-size:10px;font-weight:700}
.card-media{position:absolute;left:14px;top:36px;width:104px;height:50px;background:var(--navy);border-radius:4px}
.card-text{position:absolute;left:8px;top:88px;width:118px;font-family:"Open Sans",Arial,sans-serif;font-size:6.2px;line-height:1.35}
.meter{position:absolute;left:14px;top:118px;width:103px;height:7px;background:var(--navy);border-radius:4px;overflow:hidden}
.meter span{display:block;width:68%;height:100%;background:var(--green)}
.meter-label{position:absolute;top:127px;width:100%;font-family:"Open Sans",Arial,sans-serif;font-size:6px;font-weight:700}
.pill{position:absolute;height:10px;background:var(--navy);color:var(--white);border-radius:5px;font-family:"Open Sans",Arial,sans-serif;font-size:5.6px;line-height:10px}
.pill-invested{left:25px;top:140px;width:83px}
.pill-backers{left:12px;top:155px;width:63px}
.pill-days{left:78px;top:155px;width:44px}
.invest{position:absolute;left:26px;top:175px;width:81px;height:24px;background:var(--navy);border-radius:5px;color:var(--green);font-weight:700;font-size:13px;line-height:24px}
.view-all{left:245px;top:862px;width:256px;height:49px;border-radius:8px;text-align:center;box-shadow:inset 0 2px 0 #4f8fc4}
.view-all strong{display:block;margin-top:13px;font-size:13px}
.view-all small{display:block;font-size:6px;font-family:"Open Sans",Arial,sans-serif}

/* footer */
.footer-rule{left:0;top:921px;width:768px;height:21px;background:var(--grey-band)}
.footer{left:0;top:942px;width:768px;height:200px}
.footer-note{left:0;top:1036px;width:768px;text-align:center;font-size:11px}
.footer-base{left:0;top:1142px;width:768px;height:58px;background:var(--grey-band)}
.footer-mark{left:84px;top:1084px;width:78px;height:78px;border-radius:50%;background:var(--navy);border:4px solid #c8cbce}
.social{left:533px;top:1156px;display:flex;gap:6px;list-style:none}
.social li{width:24px;height:24px;border-radius:4px;background:#6f7c86}
</style>
</head>
<body>
<div class="abs top-strip"></div>
<header class="abs header blue-grad"></header>
<div class="abs header-rule"></div>
<a class="abs account-tab tab-login">LOGIN</a>
<a class="abs account-tab tab-register">REGISTRATION</a>
<div class="abs brand"><span class="brand-mark"></span><span class="brand-name">Fund Harbor</span></div>
<div class="abs tagline">SAFETY | SECURITY | MONEY VAULT</div>
<div class="abs search">SEARCH<span class="search-clear"></span></div>
<div class="abs language">ENGLISH<svg width="9" height="8" viewBox="0 0 9 8"><path d="M1 2l3.5 3.5L8 2" stroke="#111" stroke-width="2" fill="none"/></svg></div>

<ul class="abs stats blue-grad">
  <li><span class="tick"><svg width="11" height="9" viewBox="0 0 11 9"><path d="M1 4.5l3 3L10 1" stroke="#fff" stroke-width="2.2" fill="none"/></svg></span>$50 000 000 OF INVESTMENTS</li>
  <li><span class="tick"><svg width="11" height="9" viewBox="0 0 11 9"><path d="M1 4.5l3 3L10 1" stroke="#fff" stroke-width="2.2" fill="none"/></svg></span>1600 START-UPS</li>
  <li><span class="tick"><svg width="11" height="9" viewBox="0 0 11 9"><path d="M1 4.5l3 3L10 1" stroke="#fff" stroke-width="2.2" fill="none"/></svg></span>700 ORGANIZATIONS</li>
  <li><span class="tick"><svg width="11" height="9" viewBox="0 0 11 9"><path d="M1 4.5l3 3L10 1" stroke="#fff" stroke-width="2.2" fill="none"/></svg></span>10 000 INVESTORS</li>
  <li><span class="tick"><svg width="11" height="9" viewBox="0 0 11 9"><path d="M1 4.5l3 3L10 1" stroke="#fff" stroke-width="2.2" fill="none"/></svg></span>5000 EMPLOYEES</li>
  <li><span class="tick"><svg width="11" height="9" viewBox="0 0 11 9"><path d="M1 4.5l3 3L10 1" stroke="#fff" stroke-width="2.2" fill="none"/></svg></span>2000 PARTNERS</li>
  <li><span class="tick"><svg width="11" height="9" viewBox="0 0 11 9"><path d="M1 4.5l3 3L10 1" stroke="#fff" stroke-width="2.2" fill="none"/></svg></span>$10 000 000 OF PROFIT</li>
</ul>

<a class="abs nav-btn blue-grad" style="left:329px;width:105px">HOW STUFF WORKS?</a>
<a class="abs nav-btn blue-grad" style="left:444px;width:105px">PROJECTS REVIEW</a>
<a class="abs nav-btn blue-grad" style="left:558px;width:105px">VIRTUAL OFFICE</a>

<div class="abs video" role="img" aria-label="Introductory video player">
  <div class="video-bar">
    <span class="play"><svg width="7" height="8" viewBox="0 0 7 8"><path d="M0 0l7 4-7 4z" fill="#ddd"/></svg></span>
    <span class="progress"><span></span></span>
    <svg width="11" height="12" viewBox="0 0 11 12"><path d="M0 4h3l5-4v12l-5-4H0z" fill="#3e4144"/></svg>
    <span class="screen-btn"></span>
  </div>
</div>

<div class="abs band-grey"></div>
<div class="abs band blue-grad"></div>
<div class="abs band-mark"></div>

<a class="abs category blue-grad" style="left:85px;width:135px">RECOMMENDED</a>
<a class="abs category blue-grad" style="left:233px;width:133px">POPULAR</a>
<a class="abs category blue-grad" style="left:380px;width:135px">MOST INVESTED</a>
<a class="abs category blue-grad" style="left:528px;width:135px">NEW</a>

<article class="abs card" style="left:85px">
  <div class="stars">★★★★★</div><h3 class="card-title">PROJECT A</h3>
  <div class="card-media" role="img" aria-label="Project A preview image"></div>
  <p class="card-text">Lorem ipsum dolor sit amet, consectetur adipiscing elit. Nulla quam velit, vulputate eu pharetra</p>
  <div class="meter"><span></span></div><div class="meter-label">75% SUCCESS</div>
  <span class="pill pill-invested">$90 000 INVESTED</span><span class="pill pill-backers">200 000 INVESTORS</span><span class="pill pill-days">23 DAYS LEFT</span>
  <a class="invest">INVEST</a>
</article>
<article class="abs card" style="left:233px">
  <div class="stars">★★★★★</div><h3 class="card-title">PROJECT B</h3>
  <div class="card-media" role="img" aria-label="Project B preview image"></div>
  <p class="card-text">Lorem ipsum dolor sit amet, consectetur adipiscing elit. Nulla quam velit, vulputate eu pharetra</p>
  <div class="meter"><span></span></div><div class="meter-label">75% SUCCESS</div>
  <span class="pill pill-invested">$90 000 INVESTED</span><span class="pill pill-backers">200 000 INVESTORS</span><span class="pill pill-days">23 DAYS LEFT</span>
  <a class="invest">INVEST</a>
</article>
<article class="abs card" style="left:380px">
  <div class="stars">★★★★★</div><h3 class="card-title">PROJECT C</h3>
  <div class="card-media" role="img" aria-label="Project C preview image"></div>
  <p class="card-text">Lorem ipsum dolor sit amet, consectetur adipiscing elit. Nulla quam velit, vulputate eu pharetra</p>
  <div class="meter"><span></span></div><div class="meter-label">75% SUCCESS</div>
  <span class="pill pill-invested">$90 000 INVESTED</span><span class="pill pill-backers">200 000 INVESTORS</span><span class="pill pill-days">23 DAYS LEFT</span>
  <a class="invest">INVEST</a>
</article>
<article class="abs card" style="left:528px">
  <div class="stars">★★★★★</div><h3 class="card-title">PROJECT D</h3>
  <div class="card-media" role="img" aria-label="Project D preview image"></div>
  <p class="card-text">Lorem ipsum dolor sit amet, consectetur adipiscing elit. Nulla quam velit, vulputate eu pharetra</p>
  <div class="meter"><span></span></div><div class="meter-label">75% SUCCESS</div>
  <span class="pill pill-invested">$90 000 INVESTED</span><span class="pill pill-backers">200 000 INVESTORS</span><span class="pill pill-days">23 DAYS LEFT</span>
  <a class="invest">INVEST</a>
</article>

<a class="abs view-all blue-grad"><strong>VIEW ALL PROJECTS</strong><small>MORE THAN 1000 PROJECTS</small></a>

<div class="abs footer-rule"></div>
<footer class="abs footer blue-grad"></footer>
<p class="abs footer-note">LOTS INTERESTING INFOMATION ABOUT THE PROJECTS AND MORE</p>
<div class="abs footer-base"></div>
<div class="abs footer-mark"></div>
<ul class="abs social" aria-label="Social links"><li></li><li></li><li></li><li></li><li></li></ul>
</body>
</html>
```